This book will apply the 12 Steps to gaming addiction, also known as video game addiction. The primary purpose of the book is to provide an effective solution for this new type of addiction. The solution is based on the rich and successful concepts of traditional twelve-step programs like RL.

The title on the cover will be "Nine Doors Past the Glowing Screen" and "by Martin Quorby". A subtitle can be used if it works in your design of "A Practical Path Beyond Compulsive Console Play". Cover will be for a 6" x 9" book approximately 110 pages in length.

Some back cover text including some review quotes and an author bio are in the attached Word doc. There is also an author photo attached for for the back cover.

Requirements
Must have
• For the cover design it could be stylized, or an image, a partial image, or whatever. I am open to suggestions. Think about what would be noticed by a person searching for help with moderating their video game use, or by the parents or loved ones of problem gamers. Something contemporary and eye catching.

```html
<!DOCTYPE html>
<html lang="en">
<head>
<meta charset="UTF-8">
<title>Nine Doors Past the Glowing Screen — Cover</title>
<link rel="stylesheet" href="https://fonts.googleapis.com/css2?family=Montserrat:wght@500;600;700;800&display=swap">
<style>
  :root {
    --stage: #e4e4e4;
    --cover-deep: #0a2f73;
    --cover-mid: #0b4596;
    --cover-glow: #0b6cc2;
    --title-white: #f2f2f2;
    --title-shadow: rgba(0, 0, 0, 0.55);
    --author-cyan: #5cd3e6;
    --art-navy: #231f6e;
    --art-lavender: #8f98e0;
  }
  html, body {
    margin: 0;
    padding: 0;
    width: 1200px;
    height: 943px;
    overflow: hidden;
    background: var(--stage);
  }
  .canvas {
    position: relative;
    width: 1200px;
    height: 943px;
  }
  .cover {
    position: absolute;
    left: 310px;
    top: 41px;
    width: 580px;
    height: 860px;
    background:
      radial-gradient(ellipse 70% 55% at 50% 62%, var(--cover-glow) 0%, var(--cover-mid) 55%, var(--cover-deep) 100%);
    font-family: "Montserrat", sans-serif;
    color: var(--title-white);
    overflow: hidden;
    box-shadow: 0 10px 30px rgba(0, 0, 0, 0.18);
  }
  .title-kicker {
    position: absolute;
    left: 62px;
    top: 36px;
    margin: 0;
    font-size: 52px;
    font-weight: 700;
    letter-spacing: 4px;
    line-height: 1;
    text-shadow: 2px 3px 4px var(--title-shadow);
  }
  .title-main {
    position: absolute;
    left: 56px;
    top: 92px;
    margin: 0;
    font-size: 150px;
    font-weight: 800;
    letter-spacing: -4px;
    line-height: 1;
    text-shadow: 3px 5px 6px var(--title-shadow);
  }
  .title-line {
    position: absolute;
    left: 62px;
    top: 252px;
    margin: 0;
    font-size: 36px;
    font-weight: 600;
    line-height: 1;
    text-shadow: 1px 2px 3px var(--title-shadow);
  }
  .cover-art {
    position: absolute;
    left: 112px;
    top: 304px;
    width: 360px;
    height: 382px;
    border-radius: 28px;
    background:
      radial-gradient(ellipse 60% 45% at 62% 28%, var(--art-lavender) 0%, rgba(143, 152, 224, 0) 70%),
      linear-gradient(180deg, rgba(35, 31, 110, 0.55) 0%, var(--art-navy) 60%, rgba(35, 31, 110, 0.85) 100%);
  }
  .subtitle {
    position: absolute;
    left: 0;
    right: 0;
    top: 708px;
    margin: 0;
    text-align: center;
    font-size: 18.5px;
    font-weight: 500;
    line-height: 1;
  }
  .author {
    position: absolute;
    left: 0;
    right: 0;
    top: 810px;
    margin: 0;
    text-align: center;
    font-size: 32px;
    font-weight: 700;
    letter-spacing: 1px;
    line-height: 1;
    color: var(--author-cyan);
  }
</style>
</head>
<body>
  <main class="canvas">
    <article class="cover">
      <h1>
        <span class="title-kicker">Nine</span>
        <span class="title-main">Doors</span>
        <span class="title-line">Past the Glowing Screen</span>
      </h1>
      <div class="cover-art" role="img" aria-label="Flat illustration of a large game controller in front of a game screen, with a young person sitting on top using a laptop and another sitting below looking at a phone"></div>
      <p class="subtitle">A Practical Path Beyond Compulsive Console Play</p>
      <p class="author">Martin Quorby</p>
    </article>
  </main>
</body>
</html>
```